National Golf Software business needs banner ad designs

Our software company looks after golf clubs throughout the country. Our service specialises in membership billing for the clubs and tries to convince members to change from paying their fees upfront to monthly payment by direct debit. Simple catch cries like "spread the cost of your membership across the whole year", "let us help you make your membership affordable", "Ask you club how to spread the cost of your subs" etc. We are dealing with cost conscious clubs - not the top end of the market - and their members are also cost conscious. No good being too 'high brow'. We are also dealing with older members who are fearful of change and afraid of technology - we need to be safe and reassuring yet a great way to save up front costs. We need probably 5 to 10 banners that can rotate through on our website and on our mobile product.

Target Market(s)

Golfers, typically older and afraid of technology and afraid of direct debit. Existing members of golf clubs who have paid upfront for years and don't understand why they should pay a few dollars extra each month to split their payments. Sometimes their annual fees are quite low ($300 - $400) so they cannot justify the additional $3.50 per month surcharge for splitting their fees.

Industry/Entity Type

Golf Course

Requirements
Must have
• Make the member desire to spread the cost of their annual subscriptions. Safe, reliable, frees up their disposable income. Talk to the club to find out how. Safe and secure. Club administered.
Nice to have
• Option to call us directly on a 1300 582 916 number - they will still need to go back to the club to fill in and lodge the paperwork.
Should not have
• Cheesy, in your face, aggressive

```html
<!DOCTYPE html>
<html lang="en">
<head>
<meta charset="utf-8">
<title>Golf membership direct debit banner set</title>
<link href="https://fonts.googleapis.com/css2?family=Open+Sans:wght@300;400;600;700&display=swap" rel="stylesheet">
<style>
:root{
  --green:#6e8a2d;
  --green-soft:#8fa653;
  --navy:#12163a;
  --navy-soft:#2d2f58;
  --red:#c01824;
  --red-bright:#e0140f;
  --button:#b2192b;
  --white:#ffffff;
  --grass-dark:#3e5e18;
  --grass-light:#7da23a;
}
*{box-sizing:border-box;margin:0;padding:0}
html,body{width:1134px;height:1200px;overflow:hidden;background:var(--white)}
body{position:relative;font-family:"Open Sans",Arial,sans-serif;color:var(--white)}
.banner{position:absolute;overflow:hidden}
.tall{width:160px;height:360px;top:62px}
.wide{width:480px;height:80px}
.block{position:absolute}
.photo{position:absolute}
.grass{background:linear-gradient(160deg,var(--grass-light),var(--grass-dark))}
.course{background:linear-gradient(180deg,#c9dbe6 0%,#8fb0c4 18%,#6c9a3a 30%,#4d7a22 100%)}
.beach{background:linear-gradient(180deg,#d8d4cf 0%,#c9b8a1 45%,#b99d7a 100%)}
.sunset{background:linear-gradient(180deg,#4e7f86 0%,#8a9a50 40%,#e0b935 80%,#1a1a10 100%)}
.pale{background:linear-gradient(180deg,#ffffff 0%,#f1eff8 60%,#dcd8ec 100%)}
.head{font-weight:600;text-transform:uppercase;line-height:1.12;text-align:center}
.copy{font-weight:300;line-height:1.2}
.badge{position:absolute;border-radius:50%;background:var(--white);box-shadow:0 2px 6px rgba(0,0,0,.45);
  display:flex;align-items:center;justify-content:center;color:var(--navy);font-weight:600;letter-spacing:.02em}
.cta{position:absolute;background:var(--button);border-radius:6px;display:flex;align-items:center;justify-content:center;font-weight:600;text-align:center;line-height:1.1}
.dark-word{color:var(--navy)}
.nowrap{white-space:nowrap}
</style>
</head>
<body>

<!-- Tall banner: affordable membership, golfer -->
<div class="banner tall" style="left:85px">
  <div class="block head" style="left:0;top:0;width:160px;height:82px;background:var(--green);font-size:13.5px;padding-top:7px">Let us help you<br>make your<br>membership<br>affordable</div>
  <div class="block copy" style="left:0;top:82px;width:160px;height:80px;background:var(--navy);font-size:11px;text-align:center;padding-top:32px">Direct Debit across <b style="font-weight:600">12 months</b><br>Safe and secure.<br>Club administered.</div>
  <div class="photo course" style="left:0;top:162px;width:160px;height:198px" role="img" aria-label="Golfer addressing the ball on a seaside course"></div>
  <div class="badge" style="left:114px;top:72px;width:40px;height:40px;font-size:8px">TEEPAY</div>
  <div class="cta" style="left:17px;top:318px;width:133px;height:37px;font-size:15.5px">Call Your Club</div>
</div>

<!-- Tall banner: affordable membership, beach -->
<div class="banner tall" style="left:285px">
  <div class="photo pale" style="left:0;top:120px;width:160px;height:112px" role="img" aria-label="Soft summer sky"></div>
  <div class="photo beach" style="left:0;top:228px;width:160px;height:132px" role="img" aria-label="Red flip flops standing in the sand at the water's edge"></div>
  <div class="block head" style="left:0;top:0;width:160px;height:84px;background:var(--navy);font-size:13.5px;padding-top:8px;clip-path:polygon(0 0,100% 0,100% 85%,0 100%)">Let us help you<br>make your<br>membership<br>affordable</div>
  <div class="block" style="left:0;top:78px;width:160px;height:56px;background:var(--red);clip-path:polygon(0 12%,100% 0,100% 100%,0 100%)"></div>
  <div class="block copy" style="left:0;top:90px;width:157px;font-size:10.5px;text-align:right;font-weight:400">Direct Debit across 12 months<br>Safe and secure<br>Club administered</div>
  <div class="badge" style="left:5px;top:118px;width:50px;height:50px;font-size:10px">TEEPAY</div>
  <div class="cta" style="left:20px;top:318px;width:120px;height:39px;background:rgba(110,138,45,.85);font-size:15px;font-weight:400">Call your club to<br>Find Out How</div>
</div>

<!-- Tall banner: spread the cost, sunset -->
<div class="banner tall" style="left:486px;background:var(--navy)">
  <div class="photo sunset" style="left:0;top:104px;width:160px;height:240px" role="img" aria-label="Golfer silhouette finishing a swing at sunset beside a flag"></div>
  <div class="block" style="left:0;top:0;width:160px;height:64px;background:var(--navy);font-weight:600;font-size:12.5px;line-height:1.25;text-align:center;padding-top:12px">Spread the Cost of<br>Your Membership<br>Across the Whole Year</div>
  <div class="block copy" style="left:0;top:64px;width:160px;height:40px;background:var(--green-soft);font-size:12px;text-align:center;padding-top:5px;clip-path:polygon(0 0,100% 0,95% 100%,0 100%)">Safe and secure.<br>Club administered.</div>
  <div class="badge" style="left:14px;top:175px;width:42px;height:42px;font-size:8px">TEEPAY</div>
  <div class="cta" style="left:17px;top:321px;width:126px;height:28px;font-size:12.5px;letter-spacing:.03em">CALL YOUR CLUB</div>
</div>

<!-- Tall banner: spread the cost, club and ball -->
<div class="banner tall" style="left:686px">
  <div class="photo grass" style="left:0;top:84px;width:160px;height:224px" role="img" aria-label="Iron club resting behind a golf ball on the grass"></div>
  <div class="block head" style="left:0;top:0;width:160px;height:84px;background:var(--green);font-size:12.5px;padding-top:13px;font-weight:600">Spread the cost of<br>your membership<br>across the<br><span class="dark-word">whole year</span></div>
  <div class="badge" style="left:103px;top:97px;width:48px;height:48px;font-size:9.5px">TEEPAY</div>
  <div class="block" style="left:0;top:306px;width:160px;height:54px;background:rgba(18,22,58,.9);font-size:16px;line-height:1.2;text-align:center;padding-top:6px">Call your club<br>to find out how</div>
</div>

<!-- Tall banner: ask your club, wedge -->
<div class="banner tall" style="left:886px">
  <div class="photo grass" style="left:0;top:0;width:160px;height:310px" role="img" aria-label="Wedge and golf ball lying on green grass"></div>
  <div class="block head" style="left:0;top:0;width:160px;height:78px;background:rgba(110,138,45,.85);font-size:13.5px;padding-top:4px;text-transform:none">ASK YOUR CLUB<br>HOW TO SPREAD<br>the Cost of Your Subs<br>for 12 months</div>
  <div class="block copy" style="left:0;top:78px;width:153px;height:34px;background:var(--navy);font-size:11.5px;padding:3px 0 0 9px">Safe and secure.<br>Club administered.</div>
  <div class="badge" style="left:104px;top:104px;width:54px;height:54px;font-size:11px">TEEPAY</div>
  <div class="block copy" style="left:0;top:310px;width:160px;height:50px;background:var(--red-bright);font-size:12.5px;text-align:center;padding-top:6px">Fill in a <b style="font-weight:600">Direct Debit Form</b><br>at the Club today</div>
</div>

<!-- Wide banner: ask your club -->
<div class="banner wide" style="left:85px;top:541px">
  <div class="photo grass" style="left:0;top:0;width:480px;height:80px" role="img" aria-label="Wedge and golf ball lying on green grass"></div>
  <div class="block head" style="left:116px;top:0;width:249px;height:48px;background:rgba(110,138,45,.9);font-size:14px;padding-top:4px;font-weight:400">Ask your club how to<br>spread the cost of your subs</div>
  <div class="block copy nowrap" style="left:116px;top:48px;width:249px;height:30px;background:var(--red-bright);font-size:12.5px;font-weight:400;text-align:center;padding-top:7px">Fill in a Direct Debit form at the Club today</div>
  <div class="badge" style="left:405px;top:10px;width:60px;height:60px;font-size:12px">TEEPAY</div>
</div>

<!-- Wide banner: affordable, golfer -->
<div class="banner wide" style="left:192px;top:658px">
  <div class="photo course" style="left:290px;top:0;width:190px;height:80px" role="img" aria-label="Golfer addressing the ball on a seaside course"></div>
  <div class="block" style="left:150px;top:0;width:170px;height:80px;background:var(--navy);clip-path:polygon(0 0,100% 0,82% 100%,0 100%)"></div>
  <div class="block" style="left:0;top:0;width:150px;height:80px;background:var(--green)"></div>
  <div class="block head nowrap" style="left:4px;top:6px;width:140px;font-size:14px;line-height:1.2;font-weight:400">Let us help you<br>make your<br>membership<br>affordable</div>
  <div class="badge" style="left:133px;top:22px;width:38px;height:38px;font-size:8px">TEEPAY</div>
  <div class="block copy nowrap" style="left:181px;top:6px;font-size:12px">Direct Debit<br>across <span style="font-weight:400">12 months</span></div>
  <div class="block copy nowrap" style="left:181px;top:46px;font-size:12px">Safe and secure.<br>Club administered.</div>
  <div class="cta nowrap" style="left:392px;top:9px;width:86px;height:22px;font-size:10.5px;border-radius:4px">Call Your Club</div>
</div>

<!-- Wide banner: affordable, beach -->
<div class="banner wide" style="left:326px;top:774px">
  <div class="photo beach" style="left:0;top:0;width:106px;height:80px" role="img" aria-label="Red flip flops standing in the sand"></div>
  <div class="block head nowrap" style="left:106px;top:0;width:256px;height:38px;background:var(--navy-soft);font-size:13.5px;padding-top:2px;font-weight:400">Let us help you make<br>your membership affordable</div>
  <div class="block copy nowrap" style="left:106px;top:38px;width:256px;height:42px;background:var(--green-soft);font-size:11.5px;text-align:center;padding-top:8px">Direct Debit paying your subscriptions<br>across 12 months</div>
  <div class="photo beach" style="left:362px;top:0;width:118px;height:80px;background:linear-gradient(180deg,#e6e8e4,#b9c2b8 45%,#c9b596)" role="img" aria-label="Gentle waves washing onto the beach"></div>
  <div class="badge" style="left:436px;top:4px;width:34px;height:34px;font-size:7px">TEEPAY</div>
  <div class="cta nowrap" style="left:376px;top:52px;width:98px;height:24px;font-size:14px;font-weight:400;border-radius:4px">Call Your Club</div>
</div>

<!-- Wide banner: spread the cost, sunset -->
<div class="banner wide" style="left:406px;top:891px">
  <div class="photo sunset" style="left:0;top:0;width:480px;height:80px;background:linear-gradient(90deg,#7a8a42,#d9b43a 55%,#5c7f8a)" role="img" aria-label="Golfer silhouette at sunset beside a flag"></div>
  <div class="block nowrap" style="left:0;top:0;width:280px;height:40px;background:var(--navy);font-weight:600;font-size:14px;line-height:1.25;padding:1px 0 0 4px">Spread the Cost of Your Membership<br>across the Whole Year</div>
  <div class="block nowrap" style="left:0;top:44px;width:300px;height:30px;background:var(--green-soft);font-weight:600;font-size:14px;padding:7px 0 0 3px;clip-path:polygon(0 0,100% 0,88% 100%,0 100%)">Safe and secure. Club administered.</div>
  <div class="block" style="left:0;top:74px;width:480px;height:6px;background:#1a1a10"></div>
  <div class="badge" style="left:286px;top:14px;width:34px;height:34px;font-size:7.5px">TEEPAY</div>
  <div class="cta nowrap" style="left:381px;top:56px;width:96px;height:20px;font-size:9.5px;border-radius:4px">CALL YOUR CLUB</div>
</div>

<!-- Wide banner: spread the cost, club and ball -->
<div class="banner wide" style="left:606px;top:1008px">
  <div class="photo grass" style="left:0;top:0;width:480px;height:80px" role="img" aria-label="Iron club behind a golf ball on the grass"></div>
  <div class="block head nowrap" style="left:102px;top:0;width:276px;height:40px;background:rgba(110,138,45,.92);font-size:12px;padding-top:6px;font-weight:600">Spread the cost of your membership<br>across the <span class="dark-word">whole year</span></div>
  <div class="block nowrap" style="left:102px;top:48px;width:276px;height:32px;background:rgba(18,22,58,.85);font-size:16px;text-align:center;padding-top:5px">Call your club to find out how</div>
  <div class="badge" style="left:413px;top:16px;width:48px;height:48px;font-size:9.5px">TEEPAY</div>
</div>

</body>
</html>
```